Hardware Brand Packaging Design Project

We require a design for packaging for products in the retail hardware range. Initially this will be for a set of header cards for abrasive sanding discs but we plan to add other items to the range so we are looking for a range of brand elements that can be extended to other types of packaging.
The brand name is "Lumen Ridge" and we are looking for a black or dark grey background with a subtle fine pattern to break up the solid colour. This part of the design needs to be 'expandable' so that it can be used on different pack sizes as we increase the range. Two highlight or complimentary colours will add a bit of impact and become part of the brand style.
For printing purposes we have allowed for 4 colour process plus two spot colours and we have attached one of the header card dielines as a guide.
Target Market(s)
Home owners of both gender in the 25 to 55 age range
Industry/Entity Type
Printing
Requirements
Must have
- *The brand name "Lumen Ridge" should appear in the top left hand corner and we had in mind that the word would be a shiny metal / chrome appearance in could be in the shape of a shield or spear point but are open to any other suggestions.The word can be on one line or one above the other.
*Between the bottom of the hanger hole and the edge of the card is the words ABRASIVES & ACCESSORIES
*We want a performance guarantee device circle / seal or other in the bottom left quartile of the front facing panel. Circle device on attachment shows approx position.
* The right hand 25mm of the card is to be devoted to specific information about the product in the pack. This will be done by an adhered over-sticker ( see attached die-line No 2 )
* 3 line address panel or rear of card - QRV Abrasives, 456 Lane, West Auckland, New Zealand.
* Also somewhere on rear panel "Cut, Quality Checked & Packed in New Zealand from imported materials."
Nice to have
- It would be good, but not essential, to see a rough mock-up of how this design would transfer across to a box approx 80mm across the front, 100mm deep and 250mm high.

```html
<!DOCTYPE html>
<html lang="en">
<head>
<meta charset="utf-8">
<title>Lumen Ridge – Header Card</title>
<link href="https://fonts.googleapis.com/css2?family=Oswald:wght@500;600&family=Roboto:wght@400;500&display=swap" rel="stylesheet">
<style>
  :root {
    --paper: #ffffff;
    --dieline: #e0242b;
    --brand-red: #e31e26;
    --seal-red: #d2121b;
    --ink-dark: #0d0d0d;
    --silver-light: #f2f2f2;
    --silver-mid: #b9b9b9;
    --silver-dark: #7a7a7a;
    --spark-orange: #c56a2c;
    --text-light: #f4f4f4;
  }
  html, body {
    margin: 0;
    padding: 0;
    width: 1200px;
    height: 1020px;
    overflow: hidden;
    background: var(--paper);
  }
  .header-card {
    display: block;
    width: 1200px;
    height: 1020px;
  }
  .tagline {
    font-family: "Oswald", sans-serif;
    font-weight: 500;
    font-size: 44px;
    fill: var(--text-light);
  }
  .brand-name {
    font-family: "Oswald", sans-serif;
    font-weight: 600;
    font-size: 40px;
    fill: var(--silver-light);
  }
  .origin-note, .address-line {
    font-family: "Roboto", sans-serif;
    font-weight: 500;
    font-size: 11.5px;
    fill: var(--text-light);
  }
  .seal-figure {
    font-family: "Oswald", sans-serif;
    font-weight: 600;
    font-size: 19px;
    fill: var(--paper);
  }
  .seal-arc-text {
    font-family: "Oswald", sans-serif;
    font-weight: 600;
    font-size: 11px;
    letter-spacing: 1px;
    fill: var(--paper);
  }
</style>
</head>
<body>
<svg class="header-card" viewBox="0 0 1200 1020" xmlns="http://www.w3.org/2000/svg">
  <defs>
    <clipPath id="card-shape">
      <path d="M133 42 H285 A524 524 0 0 0 950 42 H1087 A28 28 0 0 1 1115 70 V947 A28 28 0 0 1 1087 975 H950 A499 499 0 0 0 285 975 H133 A28 28 0 0 1 105 947 V70 A28 28 0 0 1 133 42 Z"/>
    </clipPath>
    <linearGradient id="spark-tones" x1="0" y1="0" x2="1" y2="0">
      <stop offset="0" stop-color="#5a5654"/>
      <stop offset="0.08" stop-color="#2a2725"/>
      <stop offset="0.25" stop-color="#1a1512"/>
      <stop offset="0.4" stop-color="#8a4a20"/>
      <stop offset="0.55" stop-color="var(--spark-orange)"/>
      <stop offset="0.7" stop-color="#6a3a1c"/>
      <stop offset="0.82" stop-color="#1c1a19"/>
      <stop offset="1" stop-color="#111"/>
    </linearGradient>
    <linearGradient id="centre-shade" x1="0" y1="0" x2="0" y2="1">
      <stop offset="0" stop-color="#000" stop-opacity="0"/>
      <stop offset="0.38" stop-color="#000" stop-opacity="0.55"/>
      <stop offset="0.5" stop-color="#000" stop-opacity="0.85"/>
      <stop offset="0.62" stop-color="#000" stop-opacity="0.55"/>
      <stop offset="1" stop-color="#000" stop-opacity="0"/>
    </linearGradient>
    <linearGradient id="silver" x1="0" y1="0" x2="1" y2="0">
      <stop offset="0" stop-color="var(--silver-dark)"/>
      <stop offset="0.5" stop-color="var(--silver-light)"/>
      <stop offset="1" stop-color="var(--silver-mid)"/>
    </linearGradient>
    <path id="seal-arc-top" d="M-44 0 A44 44 0 0 1 44 0"/>
    <path id="seal-arc-bottom" d="M-44 0 A44 44 0 0 0 44 0"/>
  </defs>

  <rect class="dieline" x="55.5" y="2.5" width="1109" height="1015" fill="none" stroke="var(--dieline)" stroke-width="1.5"/>

  <g clip-path="url(#card-shape)">
    <rect class="spark-photo" x="105" y="42" width="1010" height="933" fill="url(#spark-tones)" role="img" aria-label="Photo of a grinding disc throwing orange sparks, mirrored top and bottom"/>
    <rect class="centre-shade" x="105" y="42" width="1010" height="933" fill="url(#centre-shade)"/>

    <path class="brand-band" d="M105 388 H400 C372 440 362 495 325 507 C362 519 372 575 400 629 H105 Z" fill="var(--brand-red)"/>

    <g class="hanger-slot" fill="var(--paper)">
      <path d="M408 507 L462 343 H720 A27 27 0 0 1 720 397 H672 C652 397 648 422 630 432 C612 442 598 428 590 410 C580 390 560 386 546 398 C538 405 530 410 520 402 C505 388 488 382 474 394 L432 500 L455 507 Z"/>
      <path transform="translate(0 1014) scale(1 -1)" d="M408 507 L462 343 H720 A27 27 0 0 1 720 397 H672 C652 397 648 422 630 432 C612 442 598 428 590 410 C580 390 560 386 546 398 C538 405 530 410 520 402 C505 388 488 382 474 394 L432 500 L455 507 Z"/>
    </g>

    <g class="product-sticker-area">
      <polygon points="1003,76 1100,156 1100,863 1003,941 905,863 905,156" fill="url(#silver)"/>
      <rect x="915" y="157" width="175" height="705" fill="var(--paper)"/>
    </g>

    <g class="brand-front">
      <text class="brand-name" x="228" y="570" text-anchor="middle" textLength="222" lengthAdjust="spacingAndGlyphs">LUMEN</text>
      <text class="brand-name" x="228" y="604" text-anchor="middle" textLength="180" lengthAdjust="spacingAndGlyphs">RIDGE</text>
    </g>
    <g class="brand-back" transform="rotate(180 228 475)">
      <text class="brand-name" x="228" y="472" text-anchor="middle" textLength="222" lengthAdjust="spacingAndGlyphs">LUMEN</text>
      <text class="brand-name" x="228" y="506" text-anchor="middle" textLength="180" lengthAdjust="spacingAndGlyphs">RIDGE</text>
    </g>

    <text class="tagline" x="604" y="766" text-anchor="middle" textLength="444" lengthAdjust="spacingAndGlyphs">ABRASIVES &amp; ACCESSORIES</text>
    <text class="tagline" x="604" y="766" text-anchor="middle" textLength="444" lengthAdjust="spacingAndGlyphs" transform="rotate(180 604 504)">ABRASIVES &amp; ACCESSORIES</text>

    <g class="rear-info" transform="rotate(180 230 325)">
      <text class="origin-note" x="125" y="292">Cut, Quality Checked &amp; Packed</text>
      <text class="origin-note" x="70" y="311">in New Zealand from imported materials</text>
      <g class="factory-icon" fill="var(--paper)">
        <path d="M150 372 V340 H158 V352 L166 346 V352 L174 346 V352 L182 346 V372 Z"/>
      </g>
      <text class="address-line" x="188" y="348">QRV Abrasives,</text>
      <text class="address-line" x="188" y="363">456 Lane, West Auckland,</text>
      <text class="address-line" x="188" y="378">New Zealand.</text>
    </g>

    <g class="guarantee-seal" transform="translate(205 876)">
      <circle r="64" fill="var(--seal-red)"/>
      <circle r="54" fill="none" stroke="url(#silver)" stroke-width="5"/>
      <ellipse rx="40" ry="17" fill="url(#silver)"/>
      <ellipse rx="36" ry="14" fill="var(--seal-red)"/>
      <text class="seal-figure" y="7" text-anchor="middle">100%</text>
      <text class="seal-arc-text" dy="-4"><textPath href="#seal-arc-top" startOffset="50%" text-anchor="middle">TOP QUALITY</textPath></text>
      <text class="seal-arc-text" dy="12"><textPath href="#seal-arc-bottom" startOffset="50%" text-anchor="middle">GUARANTEE</textPath></text>
    </g>
    <g class="guarantee-seal" transform="translate(197 132) rotate(180)">
      <circle r="64" fill="var(--seal-red)"/>
      <circle r="54" fill="none" stroke="url(#silver)" stroke-width="5"/>
      <ellipse rx="40" ry="17" fill="url(#silver)"/>
      <ellipse rx="36" ry="14" fill="var(--seal-red)"/>
      <text class="seal-figure" y="7" text-anchor="middle">100%</text>
      <text class="seal-arc-text" dy="-4"><textPath href="#seal-arc-top" startOffset="50%" text-anchor="middle">TOP QUALITY</textPath></text>
      <text class="seal-arc-text" dy="12"><textPath href="#seal-arc-bottom" startOffset="50%" text-anchor="middle">GUARANTEE</textPath></text>
    </g>
  </g>
</svg>
</body>
</html>
```